Where Quiet Rivers Carry Us

I have a previously designed book cover, and although I am mostly happy with it, I do not care for the photo on the cover of the book. I would like to keep the fonts and scrollwork on the current book cover (the brown outer edge is optional).
I prefer a Christian focus with a soft, gentle, grieving, trusting feeling of a mother as God leads without the typical religious symbols (ie: huge hands, overwhelming crosses, Heaven opening). Softly toned or small Christian icons would be acceptable.
The book dimensions are 5.5 X 8.5 and the spine is 1/2" thick.
Original book cover is here: http://wherequietriverscarryus.pinebrookpages.net/p/free-books.html
Back cover book description (two photos and the logo for the back cover can be found below) :
For I am the Lord your God who takes hold of your right hand and says to you, "Do not fear, I will help you." Isaiah 41:13
One day you were here, Colby, the next you were at the throne of God. How I long to know what heaven is like so I can envision where you are. Are you talking to Gideon about the battles of old? Are you asking Paul about the stonings, the scales, and the shipwrecks? Or are you still just standing in awe of the God and Savior that your mother could never have come close to describing to you? How I long to stand in awe with you, praising the God who gives and takes away. Just like I told you all those times when you were here with us, "If you go first, I'll see you when I get there, my son." Love you, Mom
On Friday, February 18, 2011, God did the unthinkable in our lives: He chose to take our 12-year-old son, Colby, home to heaven in a skiing accident. It is only considered the unthinkable because our plans are not God's plans and our ways are not God's ways. Follow along on my journey through the valley of the shadow of death as my Savior, Jesus Christ, leads me.
(Author info)
Janna L. Voskuilen lives on a small farm in northern Wisconsin with her husband, Dale, and their children. Experiencing the tragic death of her son has caused her to draw closer to God as He leads her down an unexpected path to know Him better.
I have updated the back cover details to include the exact words for the back cover as well as two photos and a logo. Thank you, designers, for sharing your creativity!
Reason: Still looking for the perfect book cover!
Reason: Still looking for the perfect design!
Working on final revisions!

```html
<!DOCTYPE html>
<html lang="en">
<head>
<meta charset="utf-8">
<title>Where Quiet Rivers Carry Us – Book Cover</title>
<link rel="stylesheet" href="https://fonts.googleapis.com/css2?family=Crimson+Text:ital,wght@0,400;0,700;1,400&family=Great+Vibes&display=swap">
<style>
  :root{
    --parchment-light:#f1d9a0;
    --parchment-mid:#e6b86a;
    --parchment-edge:#c98a3a;
    --crimson:#9c1016;
    --crimson-dark:#6e0a0e;
    --spine-red:#b5141b;
    --ink:#3b2a1a;
    --gold:#e8c77a;
    --cream:#f6e7c6;
    --panel-dark:#0d0907;
    --glow:#fff4c8;
  }
  *{margin:0;padding:0;box-sizing:border-box}
  html,body{width:1200px;height:887px;overflow:hidden;background:#fff}
  .cover{
    position:relative;width:1200px;height:887px;overflow:hidden;
    background:radial-gradient(ellipse at 40% 45%,var(--parchment-light) 0%,var(--parchment-mid) 65%,var(--parchment-edge) 100%);
  }

  /* Back cover */
  .back-verse{
    position:absolute;left:60px;top:52px;width:480px;text-align:center;
    font-family:"Great Vibes",cursive;font-weight:400;color:var(--crimson);
    font-size:27px;line-height:32px;
  }
  .back-verse .ref{display:block;padding-left:150px}
  .back-copy{
    position:absolute;left:79px;top:222px;width:418px;
    font-family:"Crimson Text",serif;font-style:italic;color:var(--ink);
    font-size:13.6px;line-height:26.4px;text-align:justify;
  }
  .back-copy p+p{margin-top:18px}
  .photo{
    position:absolute;top:600px;height:108px;border:2px solid var(--crimson-dark);
  }
  .photo-mother{left:74px;width:80px;background:linear-gradient(160deg,#8a6a48,#4a3726)}
  .photo-son{left:163px;width:91px;background:linear-gradient(160deg,#6f7a52,#3e3a28)}
  .ministry-name{
    position:absolute;left:345px;top:652px;width:163px;
    display:flex;align-items:center;justify-content:center;gap:8px;
    font-family:"Crimson Text",serif;font-style:italic;font-weight:400;
    color:var(--ink);font-size:17px;line-height:20px;white-space:nowrap;
  }
  .ministry-name::before{
    content:"";width:9px;height:9px;border-radius:50%;background:var(--ink);flex:none;
  }
  .author-bio{
    position:absolute;left:53px;top:730px;width:469px;height:96px;
    background:var(--crimson);padding:10px 14px;
    font-family:"Crimson Text",serif;font-style:italic;color:var(--cream);
    font-size:13.4px;line-height:25.5px;
  }

  /* Spine */
  .spine{
    position:absolute;left:574px;top:0;width:52px;height:887px;
    background:linear-gradient(90deg,var(--crimson-dark),var(--spine-red) 45%,var(--crimson-dark));
  }
  .spine-title,.spine-author{
    position:absolute;left:50%;white-space:nowrap;
    font-family:"Great Vibes",cursive;
    transform:translate(-50%,-50%) rotate(90deg);
  }
  .spine-title{top:423px;font-size:22px;color:#e99a8a}
  .spine-author{top:760px;font-size:21px;color:var(--gold)}

  /* Front cover */
  .front{
    position:absolute;left:666px;top:40px;width:493px;height:808px;
    background:radial-gradient(ellipse at 55% 55%,#2a1a0c 0%,var(--panel-dark) 60%);
    box-shadow:0 0 0 2px #3a0a0a;
  }
  .front-frame{
    position:absolute;inset:8px;border:1.5px solid var(--crimson);
    box-shadow:inset 0 0 0 3px var(--panel-dark),inset 0 0 0 4px var(--crimson);
  }
  .front-art{
    position:absolute;left:60px;top:170px;width:372px;height:520px;
    background:radial-gradient(ellipse at 50% 40%,var(--glow) 0%,#e6b24c 22%,#7a4a14 48%,rgba(13,9,7,0) 72%);
  }
  .scroll{position:absolute;background:radial-gradient(ellipse,rgba(150,150,150,.35),rgba(150,150,150,0) 70%)}
  .scroll-top{right:0;top:0;width:114px;height:102px}
  .scroll-bottom{left:-56px;bottom:0;width:104px;height:130px;
    background:radial-gradient(ellipse,rgba(150,90,40,.4),rgba(150,90,40,0) 70%)}
  .front-title{
    position:absolute;left:0;right:0;top:52px;text-align:center;
    font-family:"Great Vibes",cursive;font-weight:400;color:var(--gold);
    font-size:44px;line-height:58px;
  }
  .front-author{
    position:absolute;left:0;right:0;bottom:40px;text-align:center;
    font-family:"Great Vibes",cursive;color:var(--cream);font-size:24px;
  }
</style>
</head>
<body>
<main class="cover">

  <section class="back">
    <h2 class="back-verse">For I am the Lord your God who takes<br>hold of your right hand and says to you,<br>“Do not fear, I will help you.”<span class="ref">Isaiah 41:13</span></h2>
    <div class="back-copy">
      <p>One day you were here, Colby, the next you were at the throne of God. How I long to know what heaven is like so I can envision where you are. Are you talking to Gideon about the battles of old? Are you asking Paul about the stonings, the scales, and the shipwrecks? Or are you still just standing in awe of the God and Savior that your mother could never have come close to describing to you? How I long to stand in awe with you, praising the God who gives and takes away. Just like I told you all those times when you were here with us, “If you go first, I’ll see you when I get there, my son.” Love you, Mom</p>
      <p>On Friday, February 18, 2011, God did the unthinkable in our lives: He chose to take our 12-year-old son, Colby, home to heaven in a skiing accident. It is only considered the unthinkable because our plans are not God’s plans and our ways are not God’s ways. Follow along on my journey through the valley of the shadow of death as my Savior, Jesus Christ, leads me.</p>
    </div>
    <div class="photo photo-mother" role="img" aria-label="Portrait photo of the author"></div>
    <div class="photo photo-son" role="img" aria-label="Portrait photo of the author's son"></div>
    <p class="ministry-name">Still Waters Ministries</p>
    <p class="author-bio">Janna L. Voskuilen lives on a small farm in northern Wisconsin with her husband, Dale, and their children. Experiencing the tragic death of her son has caused her to draw closer to God as He leads her down an unexpected path to know Him better.</p>
  </section>

  <section class="spine">
    <span class="spine-title">Where Quiet Rivers Carry Us</span>
    <span class="spine-author">Janna L. Voskuilen</span>
  </section>

  <section class="front">
    <div class="front-art" role="img" aria-label="Glowing light shining in the darkness"></div>
    <div class="front-frame"></div>
    <div class="scroll scroll-top" role="img" aria-label="Decorative scrollwork"></div>
    <div class="scroll scroll-bottom" role="img" aria-label="Decorative scrollwork"></div>
    <h1 class="front-title">Where Quiet<br>Rivers Carry Us</h1>
    <p class="front-author">Janna L. Voskuilen</p>
  </section>

</main>
</body>
</html>
```